Flyer design

We need a marketing flyer to use when meeting with clients. We may also use it for mailings. Please see the attached document and images. Not all images need to be used. Please feel free to edit / photoshop images. Please also see our website : www.kelvorantissue.com

Industry/Entity Type

Marketing

```html
<!DOCTYPE html>
<html lang="en">
<head>
<meta charset="utf-8">
<title>Kelvoran Tissue Diagnostics – Flyer</title>
<link rel="stylesheet" href="https://fonts.googleapis.com/css2?family=Didact+Gothic&family=Montserrat:wght@700&display=swap">
<style>
  :root {
    --page-bg: #ecebea;
    --paper: #ffffff;
    --ink: #2b2b2b;
    --brand-red: #e01e26;
    --brand-dark: #231f20;
    --tissue-light: #f2b4c0;
    --tissue-mid: #e58a9e;
    --tissue-deep: #c9607c;
    --suit: #2a2d36;
    --footer-bg: #232224;
    --footer-text: #e6e6e6;
  }
  * { box-sizing: border-box; margin: 0; padding: 0; }
  html, body {
    width: 1200px; height: 1200px; overflow: hidden;
    background: var(--page-bg);
    font-family: "Didact Gothic", "Century Gothic", sans-serif;
    color: var(--ink);
  }
  .flyer {
    position: absolute; left: 204px; top: 40px;
    width: 792px; height: 1120px;
    background: var(--paper);
    box-shadow: 0 6px 24px rgba(0,0,0,0.18);
    overflow: hidden;
  }
  .hero-tissue {
    position: absolute; left: 0; top: 150px; width: 792px; height: 522px;
    background:
      radial-gradient(ellipse at 85% 25%, #f3c39b 0%, rgba(243,195,155,0) 35%),
      radial-gradient(ellipse at 30% 40%, var(--tissue-light) 0%, rgba(242,180,192,0) 55%),
      linear-gradient(120deg, var(--tissue-mid) 0%, var(--tissue-deep) 45%, var(--tissue-mid) 100%);
  }
  .hero-portrait {
    position: absolute; left: 370px; top: 252px; width: 422px; height: 420px;
    background: linear-gradient(180deg, #6b5a55 0%, var(--suit) 45%, #1f222a 100%);
    border-radius: 180px 180px 0 0;
  }
  .hero-wave {
    position: absolute; left: 0; top: 0; width: 792px; height: 300px;
  }
  .brand {
    position: absolute; left: 70px; top: 150px;
    display: flex; align-items: center; gap: 12px;
  }
  .brand-dot {
    width: 22px; height: 22px; border-radius: 50%; background: var(--brand-red);
  }
  .brand-name {
    font-size: 20px; letter-spacing: 1px; color: var(--brand-dark);
  }
  .headline {
    position: absolute; left: 75px; top: 362px;
    font-size: 38px; line-height: 1.1; color: #fff; font-weight: 400;
    text-shadow: 0 2px 4px rgba(0,0,0,0.35);
  }
  .physician {
    position: absolute; left: 75px; top: 568px; color: #fff;
    text-shadow: 0 1px 3px rgba(0,0,0,0.4);
  }
  .physician-name {
    font-family: "Montserrat", Arial, sans-serif; font-weight: 700; font-size: 20px;
  }
  .physician-cred { font-size: 16px; line-height: 1.15; }
  .services {
    position: absolute; left: 78px; top: 700px; width: 650px;
    font-size: 16px; line-height: 1.3;
  }
  .services p { margin-bottom: 8px; }
  .services .gap { margin-top: 22px; }
  .footer {
    position: absolute; left: 0; bottom: 0; width: 792px; height: 62px;
    background: var(--footer-bg); color: var(--footer-text);
    display: flex; align-items: center; justify-content: center;
    font-size: 12.5px; letter-spacing: 0.2px;
  }
  .footer .sep { margin: 0 9px; }
</style>
</head>
<body>
  <main class="flyer">
    <div class="hero-tissue" role="img" aria-label="Pink stained skin tissue micrograph background"></div>
    <div class="hero-portrait" role="img" aria-label="Portrait photo of the dermatopathologist in a dark suit, arms crossed"></div>
    <svg class="hero-wave" viewBox="0 0 792 300" aria-hidden="true">
      <path d="M0 0 H792 V190 C700 188 640 230 560 225 C430 215 300 300 160 290 C90 285 40 260 0 240 Z" fill="#ffffff"/>
    </svg>

    <div class="brand">
      <span class="brand-dot"></span>
      <span class="brand-name">Kelvoran Tissue Diagnostics</span>
    </div>

    <h1 class="headline">The Diagnosis<br>in Focus.</h1>

    <div class="physician">
      <div class="physician-name">Daniel R. Maren, M.D.</div>
      <div class="physician-cred">Board Certified – Dermatopathology</div>
      <div class="physician-cred">Board Certified – Dermatology</div>
    </div>

    <section class="services">
      <p>Committed to helping find solutions, either in-house or through our contacts, for all your dermatopathology needs including but not limited to:</p>
      <p>Dermatopathology consultative service – First or second opinions, off-site or<br>on-site.</p>
      <p>Tissue processing</p>
      <p>Immunohistochemistry and special stains</p>
      <p class="gap">Practicing Dermatopathology since 2007.</p>
      <p>Access to an extensive range of special and immunohistochemistry stains, and patient-centered consideration of the judicious use of them.</p>
      <p class="gap">Usually 2-3 day turnaround time.</p>
      <p>Courier pick up can usually be arranged.</p>
    </section>

    <footer class="footer">
      <span>1480 Harbor Crest Avenue, Suite 204, Seaview, CA 90412</span>
      <span class="sep">|</span>
      <span>T: (555) 318-4720</span>
      <span class="sep">|</span>
      <span>www.kelvorantissue.com</span>
    </footer>
  </main>
</body>
</html>
```